Visitenkarten-Design für aufstrebendes, modernes und innovatives Elektrounternehmen
Zielgruppe
Unsere Firma ist im Bereich Elektro- und Gebäudetechnik angesiedelt.
Zielgruppe sind Privatkunden und Geschäftskunden.
Wir machen alles rund um das Thema Elektrotechnik, Elektroinstallation ....
Aufgabenstellung
Es soll ein ansprechendes modernes Design sein. Gerne auch mit Rückseite.
Wir sind ein junges aufstrebendes modernes und innovatives Unternehmen

```html
<!DOCTYPE html>
<html lang="de">
<head>
<meta charset="utf-8">
<title>voltaro – Visitenkarte</title>
<link rel="stylesheet" href="https://fonts.googleapis.com/css2?family=Arimo:wght@400;700&display=swap">
<style>
  :root {
    --paper: #ffffff;
    --backdrop: #f3f4f6;
    --card-edge: #6b6b6b;
    --olive: #b5aa0c;
    --olive-pale: #efecc6;
    --slate: #5b5c5e;
    --teal: #1f9bb1;
    --navy: #1f3b7a;
    --ink: #333333;
    --muted: #6a6a6a;
  }
  * { margin: 0; padding: 0; box-sizing: border-box; }
  html, body {
    width: 1200px; height: 807px; overflow: hidden;
    background: var(--backdrop);
    font-family: "Arimo", Arial, sans-serif;
  }
  .sheet { position: relative; width: 1200px; height: 807px; }
  .card {
    position: absolute; left: 362px; width: 476px;
    background: var(--paper);
    border: 1px solid var(--card-edge);
    overflow: hidden;
  }
  .card--front { top: 72px; height: 301px; }
  .card--back { top: 412px; height: 303px; }

  .brand-mark {
    position: absolute; left: 99px; top: 116px;
    width: 68px; height: 68px; border-radius: 50%;
    background: var(--olive);
  }
  .brand-name {
    position: absolute; left: 178px; top: 118px;
    font-size: 50px; font-weight: 700; line-height: 1;
    color: var(--slate); letter-spacing: 0.5px;
  }
  .brand-tagline {
    position: absolute; left: 192px; top: 168px;
    font-size: 11.5px; font-weight: 700; color: var(--teal);
    letter-spacing: 0.3px;
  }

  .back-circle {
    position: absolute; left: -26px; top: 100px;
    width: 290px; height: 290px; border-radius: 50%;
    background: var(--olive-pale);
  }
  .person { position: absolute; left: 28px; top: 153px; }
  .person-name { font-size: 16px; font-weight: 700; color: var(--navy); }
  .person-role { font-size: 12.5px; color: var(--muted); margin-top: 3px; }
  .contact {
    position: absolute; left: 262px; top: 155px;
    list-style: none; font-size: 13px; line-height: 19.2px; color: var(--ink);
  }
</style>
</head>
<body>
<main class="sheet">
  <section class="card card--front" aria-label="Vorderseite">
    <span class="brand-mark" aria-hidden="true"></span>
    <span class="brand-name">voltaro</span>
    <span class="brand-tagline">ELEKTRO- &amp; GEBÄUDETECHNIK</span>
  </section>

  <section class="card card--back" aria-label="Rückseite">
    <span class="back-circle" aria-hidden="true"></span>
    <div class="person">
      <p class="person-name">Jonas Brenner</p>
      <p class="person-role">Geschäftsführer</p>
    </div>
    <ul class="contact">
      <li>Lindenweg 48</li>
      <li>D_72531 Talfeld</li>
      <li>T&nbsp; + 49 7461 254 310 72</li>
      <li>F&nbsp; + 49 7461 254 310 73</li>
      <li>M&nbsp; + 49 172 406 519 38</li>
      <li>jonas@voltaro-elektrotechnik.de</li>
      <li>www.voltaro-elektrotechnik.de</li>
    </ul>
  </section>
</main>
</body>
</html>
```